Business Cards for new orthopaedic surgery practice

My husband and I are starting our own orthopaedic surgery practice. We are looking for a business card that is uniform, but one will have my name/title and the other will have his. You can just create one design with my name on it for now. But when I choose your design as the winning design I will ask that you add another copy with his name/title.

We are looking for classy, simple, elite all in one. We like dark blues/a little gold/yellow. Something that goes with our logo. We want our logo incorporated. Here is all the info you need:
Business name: RV Spine & Vitality Center
Location: 38915 North Bramble Ave
Coral Springs, FL 33071
Phone: 954-218-4630
Fax: 954-571-2846
Email: info@myrvspine.example

Names: Lucinda Ferrow, M.D.
Board Certified Hand and Upper Extremity Surgeon

Emeka Dlunga, M.D.
Board Certified Hip & Knee Replacement/General Orthopaedic Surgeon

Can decide what you want to put on the back. Maybe a slogan:
Rooted in Care. Focused on You

I am just going to upload our logo. The only thing is if we select you as the winning design, the location, and phone numbers may change. We will need your help to update that once fully solidified.

Industry/Entity Type

Medical

Contact Information for Business Card

Colors
0054AA
0677BA
7BADD7
CADEEF
E8F1F8
0094D4
00A9DD
6FCCEA
C7EBF8
E9F6FB

Requirements
Must have
• class, appeal,
Should not have
• We want to air on the side of masculine if we are looking at masculine vs. feminine feel. But we still want it classy, sophisticated, and something we will love

```html
<!DOCTYPE html>
<html lang="en">
<head>
<meta charset="utf-8">
<title>RV Spine &amp; Vitality Center – Business Card</title>
<link href="https://fonts.googleapis.com/css2?family=Montserrat:wght@300;400;500;600;700&display=swap" rel="stylesheet">
<style>
  :root {
    --backdrop: #dedede;
    --card: #ffffff;
    --navy: #1b2a52;
    --ink: #111111;
    --grey-text: #555a63;
    --gold: #b39b73;
    --gold-bright: #c4a56c;
    --mist: #e6e6ee;
    --mist-clear: rgba(230, 230, 238, 0);
  }
  * { box-sizing: border-box; margin: 0; padding: 0; }
  html, body {
    width: 1200px; height: 1200px; overflow: hidden;
    background: var(--backdrop);
    font-family: "Montserrat", sans-serif;
  }
  .card {
    position: absolute; left: 179px; width: 861px; height: 496px;
    background: var(--card); overflow: hidden;
  }
  .card--front { top: 84px; }
  .card--back { top: 621px; }

  /* front */
  .canopy-backdrop {
    position: absolute; inset: 0;
    background:
      radial-gradient(ellipse 62% 78% at 50% 72%,
        var(--mist) 0%, var(--mist) 58%, var(--mist-clear) 100%);
  }
  .brand-ring {
    position: absolute; left: 296px; top: 114px; width: 268px; height: 268px;
    border: 2px solid var(--gold-bright); border-radius: 50%;
  }
  .brand-name-front {
    position: absolute; left: 296px; top: 114px; width: 268px; height: 268px;
    display: flex; align-items: center; justify-content: center; text-align: center;
    font-size: 28px; font-weight: 600; line-height: 1.25; color: var(--navy);
    padding: 0 30px;
  }

  /* back */
  .practice-title {
    position: absolute; left: 37px; top: 38px;
    font-size: 31px; font-weight: 700; color: var(--ink); line-height: 1;
  }
  .gold-rule {
    position: absolute; left: 37px; right: 37px; top: 90px; height: 6px;
    background: var(--gold);
  }
  .doctor {
    position: absolute; right: 37px; top: 127px; text-align: right;
  }
  .doctor-name { font-size: 30px; font-weight: 600; color: var(--navy); line-height: 1; }
  .doctor-title {
    margin-top: 12px; font-size: 22px; font-weight: 400; color: var(--grey-text); line-height: 1.4;
  }
  .brand-mark {
    position: absolute; left: 37px; top: 220px;
    display: flex; align-items: center; gap: 12px;
  }
  .brand-dot { width: 26px; height: 26px; border-radius: 50%; background: var(--navy); }
  .brand-name-back { font-size: 20px; font-weight: 600; color: var(--navy); }

  .contact-list {
    position: absolute; left: 37px; top: 320px; list-style: none;
  }
  .contact-list li { font-size: 24px; line-height: 38px; white-space: nowrap; }
  .contact-label { color: var(--navy); font-weight: 500; }
  .contact-value { color: var(--grey-text); font-weight: 300; }

  .address {
    position: absolute; right: 37px; top: 404px; text-align: right;
    font-size: 22px; font-weight: 400; line-height: 32px; color: var(--grey-text);
  }
</style>
</head>
<body>
  <section class="card card--front">
    <div class="canopy-backdrop" role="img" aria-label="Faint large tree canopy silhouette in pale grey"></div>
    <div class="brand-ring"></div>
    <div class="brand-name-front">RV Spine &amp; Vitality Center</div>
  </section>

  <section class="card card--back">
    <h1 class="practice-title">RV Spine &amp; Vitality Center</h1>
    <div class="gold-rule"></div>

    <div class="doctor">
      <p class="doctor-name">Lucinda Ferrow, M.D.</p>
      <p class="doctor-title">Board Certified Hand and<br>Upper Extremity Surgeon</p>
    </div>

    <div class="brand-mark">
      <span class="brand-dot"></span>
      <span class="brand-name-back">RV Spine &amp; Vitality Center</span>
    </div>

    <ul class="contact-list">
      <li><span class="contact-label">Phone.</span>&nbsp; <span class="contact-value">954-218-4630</span></li>
      <li><span class="contact-label">Fax.</span> <span class="contact-value">954-571-2846</span></li>
      <li><span class="contact-label">Email.</span> <span class="contact-value">info@myrvspine.example</span></li>
      <li><span class="contact-label">Website.</span> <span class="contact-value">myrvspine.example</span></li>
    </ul>

    <p class="address">38915 North Bramble Ave<br>Coral Springs, FL 33071</p>
  </section>
</body>
</html>
```